Atelier Marrow Architecture business card

We need to update our business card. We do high end custom residential, hospitality, and wellness architecture. We focus on creating unique spaces and design around the five senses, believing that architecture's true impact is not on our surroundings, but within us. We would like to see designs are instill a sense of calm awe. They should be crisp, fresh, clean, authentic, & contemporary without being sterile, overworked, or harsh. White space is important. Alternative materials are an option if natural. We have created our own logo and would like designs to incorporate it. However, we are willing to see alternatives if the logo becomes a stumbling block and you have an alternate you suggest. Card must have the following information:
Atelier Marrow Architecture, Inc.
728 Holloway Ct. NE Atlanta, GA 30318
Marcus T. Whitcombe, AIA, NCARB, LEED AP BD+C
ateliermarrow.example

Target Market(s)

Higher net worth individuals with an appreciation for design, nature, sustainability,

Industry/Entity Type

Architect

Contact Information for Business Card

See above. The title of Owner or Architect is helpful but not necessary. Minimalism should trump additional information.

Font styles to use
Serif
Sans Serif

Requirements
Must have
• It should look professional. It must use logo
Should not have
• caligraphy, animals, anything that is cute,

```html
<!DOCTYPE html>
<html lang="en">
<head>
<meta charset="utf-8">
<title>Atelier Marrow Architecture — Business Card</title>
<link rel="stylesheet" href="https://fonts.googleapis.com/css2?family=Raleway:wght@300;400;500&display=swap">
<style>
  :root {
    --backdrop: #e6e7ea;
    --card-white: #ffffff;
    --panel-grey: #dcdcde;
    --band-dark: #58585a;
    --band-darker: #4a4a4c;
    --ink: #3a3a3c;
    --ink-soft: #6b6b6e;
    --on-dark: #f2f2f2;
    --ring: #e9e9e9;
  }
  * { box-sizing: border-box; margin: 0; padding: 0; }
  html, body { width: 1200px; height: 900px; overflow: hidden; }
  body {
    background: var(--backdrop);
    font-family: "Raleway", sans-serif;
    color: var(--ink);
    position: relative;
  }
  .card {
    position: absolute;
    left: 320px;
    width: 560px;
    height: 320px;
    overflow: hidden;
    background: var(--card-white);
    box-shadow: 0 10px 30px rgba(0,0,0,.12), 0 1px 3px rgba(0,0,0,.1);
  }
  .card--front { top: 80px; }
  .card--back { top: 500px; }

  /* Front */
  .front__drawing {
    position: absolute; inset: 0 0 118px 0;
    background: linear-gradient(120deg, #fafafa 0%, #ededee 55%, #e2e2e4 100%);
  }
  .holder { position: absolute; left: 40px; top: 30px; width: 300px; }
  .holder__name {
    font-weight: 300; font-size: 28px; letter-spacing: 1.5px; color: var(--ink); white-space: nowrap;
  }
  .holder__title {
    font-weight: 400; font-size: 12px; letter-spacing: .8px; color: var(--ink-soft); margin-top: 5px; white-space: nowrap;
  }
  .holder__address {
    font-weight: 400; font-size: 11px; letter-spacing: .6px; color: var(--ink-soft); margin-top: 4px; white-space: nowrap;
  }
  .wordmark {
    position: absolute; text-align: center;
    font-weight: 400; color: var(--ink); text-transform: uppercase;
  }
  .wordmark__line { display: block; }
  .wordmark--small { right: 36px; top: 124px; }
  .wordmark--small .wordmark__line { font-size: 15px; letter-spacing: 6px; }
  .wordmark--small .wordmark__sub { font-size: 7px; letter-spacing: 6px; margin-top: 5px; color: var(--ink-soft); }
  .contact-band {
    position: absolute; left: 0; right: 0; bottom: 0; height: 118px;
    display: grid; grid-template-columns: repeat(3, 1fr);
    background: var(--band-dark);
  }
  .contact-band__cell {
    position: relative; text-align: center; padding-top: 46px;
    color: var(--on-dark); font-size: 12px; letter-spacing: .5px; line-height: 1.6;
  }
  .contact-band__cell:nth-child(2) { background: var(--band-darker); }
  .contact-icon {
    position: absolute; left: 50%; top: -24px; transform: translateX(-50%);
    width: 48px; height: 48px;
  }

  /* Back */
  .back__panel { position: absolute; inset: 0; }
  .wordmark--large { left: 0; right: 0; top: 134px; }
  .wordmark--large .wordmark__line { font-size: 26px; letter-spacing: 11px; }
  .wordmark--large .wordmark__sub { font-size: 10px; letter-spacing: 10px; margin-top: 8px; color: var(--ink-soft); }
</style>
</head>
<body>

  <section class="card card--front" aria-label="Card front">
    <div class="front__drawing" role="img" aria-label="Faint architectural line drawing of a building plan"></div>

    <div class="holder">
      <p class="holder__name">Marcus T. Whitcombe</p>
      <p class="holder__title">AIA, NCARB, LEED AP BD+C</p>
      <p class="holder__address">728 Holloway Ct. NE Atlanta, GA 30318</p>
    </div>

    <div class="wordmark wordmark--small">
      <span class="wordmark__line">Atelier Marrow</span>
      <span class="wordmark__line wordmark__sub">Architecture</span>
    </div>

    <div class="contact-band">
      <div class="contact-band__cell">
        <svg class="contact-icon" viewBox="0 0 48 48" aria-hidden="true">
          <circle cx="24" cy="24" r="22" fill="var(--band-dark)" stroke="var(--ring)" stroke-width="1.5"/>
          <rect x="18" y="14" width="12" height="20" rx="2" fill="none" stroke="var(--on-dark)" stroke-width="1.6"/>
          <line x1="22" y1="30.5" x2="26" y2="30.5" stroke="var(--on-dark)" stroke-width="1.6"/>
        </svg>
        404.555.0173<br>202.555.0148
      </div>
      <div class="contact-band__cell">
        <svg class="contact-icon" viewBox="0 0 48 48" aria-hidden="true">
          <circle cx="24" cy="24" r="22" fill="var(--band-darker)" stroke="var(--ring)" stroke-width="1.5"/>
          <rect x="15" y="17" width="18" height="13" rx="1" fill="none" stroke="var(--on-dark)" stroke-width="1.6"/>
          <polyline points="15,17 24,25 33,17" fill="none" stroke="var(--on-dark)" stroke-width="1.6"/>
        </svg>
        info@ateliermarrow.example
      </div>
      <div class="contact-band__cell">
        <svg class="contact-icon" viewBox="0 0 48 48" aria-hidden="true">
          <circle cx="24" cy="24" r="22" fill="var(--band-dark)" stroke="var(--ring)" stroke-width="1.5"/>
          <circle cx="24" cy="24" r="10" fill="none" stroke="var(--on-dark)" stroke-width="1.6"/>
          <ellipse cx="24" cy="24" rx="4.5" ry="10" fill="none" stroke="var(--on-dark)" stroke-width="1.4"/>
          <line x1="14" y1="24" x2="34" y2="24" stroke="var(--on-dark)" stroke-width="1.4"/>
        </svg>
        ateliermarrow.example
      </div>
    </div>
  </section>

  <section class="card card--back" aria-label="Card back">
    <svg class="back__panel" viewBox="0 0 560 320" preserveAspectRatio="none" aria-hidden="true">
      <rect width="560" height="320" fill="var(--card-white)"/>
      <polygon points="360,0 560,0 560,320 250,320" fill="var(--panel-grey)" opacity=".7"/>
    </svg>
    <div class="wordmark wordmark--large">
      <span class="wordmark__line">Atelier Marrow</span>
      <span class="wordmark__line wordmark__sub">Architecture</span>
    </div>
  </section>

</body>
</html>
```